DATA PROTECTION OFFICER - GENERAL DATA PROTECTION REGULATION

Our network of companies is called : KVR (KVRL-MTO FLINTS).
It is sourced and based in Brussels, Belgium, hosting the EU institutions : designers and enforcers of the GDPR (https://portal.verimunda.example/info/norm/norm-topic/record-safety_en).
We are setting up connected, empowered and visionary-interconnected organizations in each country, region or city concerned by the GDPR.
We have developed unique pedagogical methods, programs, instruments (video, softwares,…) and visionary training skills – initially and on a continuous basis – for the DPO & GDPR consultants.
Our motto is : From Challenges to Opportunities.
Our yearning is : developing soulful teams, join forces & talents with our clients.
Our most wanted reward : let us astonish you!
We opt for the best available softwares on the market for project management, data analytics, GDPR compliance, DPO assistance and in general : customer relation and enhanced communication between project members.
We contribute to bringing Artificial Intelligence and Data-Driven Mindsets in enterprises.
We perceive the GDPR as the best opportunity an organization faces to value its “gold” (its data) and offer the solutions to transform them into real-life currencies and assets… MONEY .
I guess my comments need time to be integrated and I provided a lot of text too! I would particularly encourage TW (UK) to take the best out of his several proposals to mix them in the best ONE website! Offering me many graphic elements to use for all my posts/pages... I am a prolix writer :)
Target Market(s)
SME's business leaders, HR and Legal departments, read : https://www.corvanews.example/article/us-net-story-x1/growth-of-the-record-keeping-role-a-popular-new-career-path-idXQZT4LM8PW2K
Industry/Entity Type
Legal
Coding
Coded - Design and coding required
Number of Pages Required
5+ page
Colors
Designer to choose colors to be used in the design.
Requirements
Must have
- A HUMAN APPROACH
- WE NEED TO SEE HUMANS AND NOT ONLY ROBOTS OR ELECTRONIC DEVICES.
- 1) The DPO/GDPR Logos of the companies:
- https://www.filhaven.example/sh/k82q19wtzr4mn00/BXT7peLqVbZy0ghhwrR3Kslue?dl=0
- https://www.filhaven.example/sh/r3k27tjxwq85zmp/BXB4ktVRddh_q8ml5mtBgGqej?dl=0 et DPO : https://www.filhaven.example/sh/t9w4kjh7vcq48r2/BXJsmGZfRmYuvzIkwjR4Th_b?dl=0
- OR :
- https://www.filhaven.example/sh/vakkzp3mr5zgbn/BXBTxCRQ4lXmEFWN3LRg3kR7b?dl=0
- AND :
- https://stewardmesh.docushelf.example/sites/all/_layouts/15/visitorlink.aspx?visitortoken=Q4xbbe862KMTW7HkfaM5Wq0r%2BTcnNvdj1tqKX%2FmUmQOV%3D&folderid=3_2f70b91a29a805d81c96b8636e419f7ce&rev=1&e=6b600bf144535597b9296c99cd6116c9
- 2) A surprising but human, clear, simple, white, lightning look!
- 3) WORDPRESS version so that I can edit easily and add text on existing and new pages
- We therefore pass each option and - even more so - through the sieve of this inevitable - and values-generating - ethical evaluation.
- In other words, we are doubly satisfied with EVERY solution:
- 1. As a DPO/consultant and advisor to commercial enterprises or non-profit organisations but necessarily entering into a relationship involving financial flows with the persons concerned; and
- 2. As concerned person: target of the actions envisaged, parent, child, citizen and avatar in our digital lives.
- We put personal data at the centre of our projects and internal meetings, and with clients, we therefore continue the stage of brainstorming, researching and visualising ideas in interaction with the Regulation, by analysing the ethical consequences of each option.
- We choose only solutions that are applicable to the greatest number and therefore satisfy us as citizens of an increasingly connected and digital world. We also see the Regulation as a commercial and marketing opportunity to enhance the value of personal data and develop the confidence of those concerned by respect and security in the processing of such data.
- Our ultimate test: we put ourselves in our children's shoes to test the option considered, then comment on it and evaluate it as a parent.
- NO TO INCOMPREHENSIVE LEGAL TERMS... It is simply prohibited from 25 May for all information to be communicated to the persons concerned by the Regulation!
Nice to have
- - Artificial Intelligence
- - Transhumans
- - Challenges becoming Opportunities
- - a Great Dame who Protects & Reassures (see GDPR logo)
- - Friendly communication - NOT too businesslike/cold/usual
- - Page content is available here in FRENCH then ENGLISH then DUTCH then GERMAN : https://www.filhaven.example/sh/w1hjqmzsa101zwv/BXDNsFZpQSEzpMjhvRr5ZCb?dl=0
Should not have
- A cold, bankerlike, old economy, dull outlook

```html
<!DOCTYPE html>
<html lang="en">
<head>
<meta charset="utf-8">
<title>KVR — Data Protection Officer</title>
<link rel="stylesheet" href="https://fonts.googleapis.com/css2?family=Roboto:wght@300;400;500;700&display=swap">
<style>
:root{
  --navy:#1f2a6e;
  --navy-deep:#141c52;
  --navy-mid:#2a3a8c;
  --blue:#3b57b8;
  --yellow:#f4d508;
  --ink:#222634;
  --body:#4a4d5a;
  --muted:#8a8d99;
  --line:#d9dbe4;
  --white:#ffffff;
  --pale:#f3f4f8;
}
*{box-sizing:border-box;margin:0;padding:0}
html,body{width:1200px;height:4018px;overflow:hidden}
body{font-family:'Roboto',sans-serif;color:var(--body);background:var(--white);position:relative}
section,header,footer{position:absolute;left:0;width:1200px}
.abs{position:absolute}
.tab{position:absolute;left:570px;width:60px;height:22px;background:var(--white);border-radius:30px 30px 0 0;display:flex;align-items:center;justify-content:center}
.tab svg{width:14px;height:8px}
.section-title{position:absolute;left:0;width:1200px;text-align:center;font-size:26px;font-weight:500;color:var(--ink);letter-spacing:.5px}
.section-intro{position:absolute;left:150px;width:900px;text-align:center;font-size:14px;line-height:22px;color:var(--body)}
.btn{position:absolute;display:flex;align-items:center;justify-content:center;font-size:13px;border:1px solid var(--navy);color:var(--navy);background:var(--white);border-radius:2px}

/* hero */
.hero{top:0;height:523px;background:linear-gradient(100deg,#1a2468 0%,#243481 45%,#2a4ba6 70%,#1d2f78 100%);overflow:hidden}
.hero-photo{position:absolute;left:560px;top:0;width:640px;height:523px;background:radial-gradient(ellipse at 60% 55%,#5f8fd6 0%,#2f4ea6 35%,rgba(30,44,120,0) 75%)}
.brand{position:absolute;left:102px;top:26px;display:flex;align-items:center;gap:12px}
.brand-dot{width:40px;height:40px;border-radius:50%;background:var(--yellow)}
.brand-name{font-size:30px;font-weight:500;color:var(--white);letter-spacing:1px}
.topbar{position:absolute;right:100px;top:28px;font-size:13px;color:var(--white);display:flex;gap:22px;align-items:center}
.topbar b{color:var(--yellow);font-weight:500}
.nav{position:absolute;right:95px;top:64px;display:flex;gap:30px;font-size:14px;color:var(--white)}
.nav a{color:inherit;text-decoration:none;padding-bottom:8px}
.nav a.active{color:var(--yellow);border-bottom:2px solid var(--yellow)}
.hero-kicker{position:absolute;left:102px;top:180px;font-size:26px;font-weight:500;color:var(--white)}
.hero-title{position:absolute;left:102px;top:212px;font-size:40px;font-weight:700;color:var(--yellow)}
.hero-sub{position:absolute;left:102px;top:260px;font-size:26px;font-weight:500;color:var(--white)}
.hero-text{position:absolute;left:102px;top:298px;width:540px;font-size:14px;line-height:21px;color:#dfe4f5}
.hero-btn{left:102px;top:350px;width:148px;height:44px;background:transparent;border-color:var(--white);color:var(--white)}
.dots{position:absolute;left:102px;top:458px;display:flex;gap:8px}
.dots i{width:11px;height:11px;border-radius:50%;border:1.5px solid var(--yellow)}
.dots i:first-child{background:var(--yellow)}

/* what we do */
.doing{top:523px;height:656px}
.doing-map{position:absolute;left:0;top:0;width:1200px;height:656px}
.pillar{position:absolute;width:220px;text-align:center}
.pillar h3{font-size:15px;font-weight:500;color:var(--navy);line-height:19px;margin-bottom:10px}
.pillar p{font-size:13px;line-height:19px}

/* services */
.services{top:1179px;height:600px}
.dot-field{position:absolute;left:70px;top:150px;width:190px;height:150px;background:#f7ec9a}
.svc-photo{position:absolute;left:107px;top:166px;width:322px;height:343px;background:linear-gradient(135deg,#c9c3b7,#8f8678 55%,#d7d3cc)}
.svc-btn{left:107px;top:517px;width:100px;height:34px}
.offer-title{position:absolute;left:450px;top:178px;font-size:24px;color:var(--navy)}
.offer-text{position:absolute;left:450px;top:212px;width:650px;font-size:13px;line-height:20px}
.offer-col{position:absolute;top:270px;list-style:none;font-size:12.5px;color:var(--ink)}
.offer-col li{display:flex;align-items:center;gap:10px;height:32px;border-bottom:1px solid var(--line)}
.offer-col li .ic{width:14px;height:14px;border-radius:50%;background:var(--navy);flex:none}
.offer-col li.open{border-bottom:none}
.offer-col li.offer-detail{display:block;height:auto;width:270px;margin:2px 0 8px 24px;padding:12px;border:1px solid var(--line);font-size:12px;line-height:18px;color:var(--muted)}

/* faq */
.faq{top:1790px;height:386px;background:linear-gradient(90deg,#1e2a73 0%,#273794 55%,#4f63a9 100%);overflow:hidden}
.faq-photo{position:absolute;left:840px;top:0;width:360px;height:386px;background:linear-gradient(180deg,#c6cbe0,#7d87b4 60%,#3c4a91)}
.faq-title{position:absolute;left:0;width:820px;text-align:center;top:44px;font-size:26px;font-weight:500;color:var(--white)}
.faq-col{position:absolute;top:104px;list-style:none}
.faq-col li{display:flex;align-items:center;height:34px;margin-bottom:6px;background:var(--navy-deep);color:var(--white);font-size:13px}
.faq-col li .pm{width:34px;height:34px;display:flex;align-items:center;justify-content:center;color:var(--white);font-size:18px;border-right:1px solid rgba(255,255,255,.15);margin-right:14px}
.faq-col li.faq-answer{display:block;height:auto;background:var(--blue);padding:10px 14px 10px 48px;font-size:12.5px;line-height:19px;color:#e7eaf7}
.faq-btn{left:830px;top:322px;width:98px;height:34px;background:transparent;border-color:var(--yellow);color:var(--white)}

/* opportunities */
.opps{top:2176px;height:718px}
.opp-photo-a{position:absolute;left:0;top:200px;width:603px;height:236px;background:linear-gradient(120deg,#0d1f4a,#1f5fb0 55%,#0b1636);clip-path:polygon(0 0,560px 0,603px 236px,0 236px)}
.opp-photo-b{position:absolute;left:603px;top:442px;width:597px;height:228px;background:linear-gradient(120deg,#1b2340,#4f5f84 50%,#20273d);clip-path:polygon(0 0,597px 0,597px 228px,70px 228px)}
.opp-head{position:absolute;font-size:14px;font-weight:500;color:var(--navy);letter-spacing:.3px}
.checks{position:absolute;list-style:none;font-size:13px;line-height:22px}
.checks li{display:flex;align-items:center;gap:10px;margin-bottom:6px}
.checks svg{width:15px;height:15px;flex:none}
.opp-text{position:absolute;font-size:13px;line-height:21px;width:420px}

/* blogs */
.blogs{top:2894px;height:629px}
.card{position:absolute;top:166px;width:319px}
.card-photo{height:204px}
.card h3{margin-top:30px;font-size:17px;font-weight:500;color:var(--navy);line-height:22px}
.card time{display:block;margin-top:4px;font-size:17px;color:var(--yellow);font-weight:500}
.card p{margin-top:10px;font-size:12.5px;line-height:19px}
.card .btn{position:static;width:88px;height:30px;margin-top:20px;border-color:#9aa0b6;color:var(--ink);font-size:12px}

/* contact */
.contact{top:3523px;height:402px;background:linear-gradient(100deg,#1a2468 0%,#243384 55%,#2f4ca8 100%);overflow:hidden;color:var(--white)}
.contact-glow{position:absolute;left:720px;top:0;width:480px;height:402px;background:radial-gradient(ellipse at 65% 50%,rgba(90,140,230,.55),rgba(30,45,120,0) 70%)}
.c-title{position:absolute;top:56px;font-size:18px;font-weight:500}
.field-label{position:absolute;font-size:12.5px;font-weight:500}
.field{position:absolute;height:32px;background:rgba(20,30,90,.65);border:1px solid rgba(255,255,255,.12)}
.submit{left:102px;top:320px;width:80px;height:30px;background:var(--yellow);border:none;color:var(--ink);font-weight:700;font-size:12px}
.addr{position:absolute;left:785px;top:90px;width:300px;font-size:13px;line-height:20px}
.mail{position:absolute;left:785px;top:142px;display:flex;align-items:center;gap:8px;font-size:13px}
.mail i{width:16px;height:12px;background:var(--yellow);display:block}
.map{position:absolute;left:790px;top:190px;width:202px;height:92px;background:linear-gradient(135deg,#e8ecdf,#cfd8c4 60%,#b9c9d9)}
.dir{left:785px;top:303px;width:120px;height:32px;background:transparent;border-color:var(--yellow);color:var(--white)}

/* footer */
.foot{top:3925px;height:93px}
.foot-links{position:absolute;left:102px;top:22px;font-size:13px;color:var(--ink)}
.foot-copy{position:absolute;left:102px;top:54px;font-size:12px;color:var(--muted)}
.foot-brand{position:absolute;left:900px;top:22px;display:flex;align-items:center;gap:12px}
.foot-brand .brand-name{color:var(--navy)}
</style>
</head>
<body>

<header class="hero">
  <div class="hero-photo" role="img" aria-label="Businessman holding a tablet with glowing data-protection network icons"></div>
  <div class="brand"><span class="brand-dot"></span><span class="brand-name">KVR</span></div>
  <div class="topbar"><span>Call for immediate service: <b>0-800-555-0142</b></span><span>✉ support@kvr.example</span></div>
  <nav class="nav">
    <a class="active">Home</a><a>What are We Doing</a><a>Data Protection Services</a><a>Partnership</a><a>Blogs</a><a>Contact Us</a>
  </nav>
  <div class="hero-kicker">WE OFFER</div>
  <h1 class="hero-title">HIGH QUALITY DATA PROTECTION</h1>
  <div class="hero-sub">EXPERIENCE IS ESSENTIAL</div>
  <p class="hero-text">Lorem ipsum dolor sit amet, consectetur adipiscing elit. Sed varius egestas nisl quis imperdiet. Integer quis sapien ultrices, posuere velit sit amet, aliquet tortor.</p>
  <a class="btn hero-btn">View Our Solutions</a>
  <div class="dots"><i></i><i></i><i></i><i></i></div>
  <div class="tab" style="top:501px"><svg viewBox="0 0 14 8"><path d="M1 1l6 6 6-6" fill="none" stroke="#1f2a6e" stroke-width="2"/></svg></div>
</header>

<section class="doing">
  <h2 class="section-title" style="top:72px">WHAT ARE WE DOING</h2>
  <p class="section-intro" style="top:118px">Lorem ipsum dolor sit amet, consectetur adipiscing elit. Sed varius egestas nisl quis imperdiet. Integer quis sapien ultrices, posuere velit sit amet, aliquet tortor. Morbi auctor quam eu nulla tincidunt facilisis. Aliquam massa enim, egestas tincidunt consequat.</p>
  <svg class="doing-map" viewBox="0 0 1200 656" aria-hidden="true">
    <g fill="none" stroke="#e3e5ee" stroke-width="2">
      <path d="M214 254 A 170 170 0 0 1 490 254"/>
      <path d="M372 404 A 190 190 0 0 1 549 254"/>
      <path d="M657 254 A 190 190 0 0 1 826 404"/>
      <path d="M710 254 A 170 170 0 0 1 986 254"/>
      <path d="M483 404 A 170 170 0 0 0 718 404"/>
    </g>
    <g fill="#fff" stroke="#e1e3ec" stroke-width="2">
      <circle cx="268" cy="254" r="54"/><circle cx="603" cy="254" r="54"/><circle cx="932" cy="254" r="54"/>
      <circle cx="429" cy="404" r="54"/><circle cx="772" cy="404" r="54"/>
    </g>
    <g fill="none" stroke="#1f2a6e" stroke-width="2.5" stroke-linecap="round" stroke-linejoin="round">
      <rect x="252" y="238" width="32" height="32" rx="4"/><path d="M260 238v-7M268 238v-7M276 238v-7M260 270v7M268 270v7M276 270v7M252 246h-7M252 262h-7M284 246h7M284 262h7"/>
      <circle cx="603" cy="240" r="7"/><path d="M589 268c2-10 26-10 28 0"/><circle cx="584" cy="254" r="4"/><circle cx="622" cy="254" r="4"/>
      <path d="M910 240h44v26h-28l-10 8v-8h-6z"/><circle cx="924" cy="253" r="2"/><circle cx="932" cy="253" r="2"/><circle cx="940" cy="253" r="2"/>
      <circle cx="424" cy="399" r="13"/><path d="M433 408l12 12"/>
      <rect x="758" y="400" width="28" height="22" rx="3"/><path d="M764 400v-7a8 8 0 0 1 16 0v7"/>
    </g>
  </svg>
  <div class="pillar" style="left:158px;top:322px"><h3>Artificial<br>Intelligence</h3><p>Lorem ipsum dolor sit amet, consectetur adipiscing elit. Praesent ultrice s, elit et</p></div>
  <div class="pillar" style="left:493px;top:322px"><h3>Consultancy<br>with GDPR</h3><p>Lorem ipsum dolor sit amet, consectetur adipiscing elit. Praesent ultrice s, elit et</p></div>
  <div class="pillar" style="left:822px;top:322px"><h3>Concrete Actions<br>to Develop</h3><p>Lorem ipsum dolor sit amet, consectetur adipiscing elit. Praesent ultrice s, elit et</p></div>
  <div class="pillar" style="left:319px;top:472px"><h3>Complete &amp;<br>Up to Date</h3><p>Lorem ipsum dolor sit amet, consectetur adipiscing elit. Praesent ultrice s, elit et</p></div>
  <div class="pillar" style="left:662px;top:472px"><h3>Safe &amp;<br>Secure</h3><p>Lorem ipsum dolor sit amet, consectetur adipiscing elit. Praesent ultrice s, elit et</p></div>
  <svg class="abs" style="left:593px;top:630px" width="14" height="8" viewBox="0 0 14 8"><path d="M1 1l6 6 6-6" fill="none" stroke="#1f2a6e" stroke-width="2"/></svg>
</section>

<section class="services">
  <h2 class="section-title" style="top:40px">DATA PROTECTION SERVICES</h2>
  <p class="section-intro" style="top:86px">Lorem ipsum dolor sit amet, consectetur adipiscing elit. Sed varius egestas nisl quis imperdiet. Integer quis sapien ultrices, posuere velit sit amet, aliquet tortor. Morbi auctor quam eu nulla tincidunt facilisis. Aliquam massa enim, egestas tincidunt consequat.</p>
  <div class="dot-field" role="img" aria-label="Yellow halftone dot pattern"></div>
  <div class="svc-photo" role="img" aria-label="Smiling man working on a laptop in a bright office"></div>
  <a class="btn svc-btn">Contact Now</a>
  <h3 class="offer-title">What We Offer</h3>
  <p class="offer-text">Lorem ipsum dolor sit amet, consectetur adipiscing elit. Sed varius egestas nisl quis imperdiet. Integer quis sapien ultrices, posuere velit sit amet, aliquet tortor.</p>
  <ul class="offer-col" style="left:450px;width:320px">
    <li><span class="ic"></span>Storage</li>
    <li class="open"><span class="ic"></span>Modular Infrastructure</li>
    <li class="offer-detail">Lorem ipsum dolor sit amet, consectetur adipiscing elit. Praesent ultrices, elit et sagittis fermentum, lacus augue porttitor ligula, sed imperdiet nulla elit sit amet dui.</li>
    <li><span class="ic"></span>Converged Infrastructure</li>
    <li><span class="ic"></span>High Performance Computing</li>
    <li><span class="ic"></span>Open Manage Systems</li>
  </ul>
  <ul class="offer-col" style="left:785px;width:290px">
    <li><span class="ic"></span>Data Virtualization</li>
    <li><span class="ic"></span>Safe and Secure</li>
    <li><span class="ic"></span>Open Systems</li>
    <li><span class="ic"></span>Server Platforms</li>
    <li><span class="ic"></span>Extreme Scale Infrastructure</li>
  </ul>
</section>

<section class="faq">
  <div class="faq-photo" role="img" aria-label="Businessman in glasses working on a laptop"></div>
  <div class="tab" style="top:0;border-radius:0 0 30px 30px"><svg viewBox="0 0 14 8"><path d="M1 1l6 6 6-6" fill="none" stroke="#1f2a6e" stroke-width="2"/></svg></div>
  <h2 class="faq-title">FREQUENTLY ASKED QUESTIONS</h2>
  <ul class="faq-col" style="left:102px;width:408px">
    <li><span class="pm">+</span>Nunc auctor elementum egestas. Sed a porttitor eros.</li>
    <li style="margin-bottom:0"><span class="pm">−</span>Curabitur nisi metus, molestie vitae varius</li>
    <li class="faq-answer">Lorem ipsum dolor sit amet, consectetur adipiscing elit. Nam vel dui quis nunc aliquam pellentesque sit amet pretium massa. Integer sollicitudin eros justo, vel pulvinar purus.</li>
    <li><span class="pm">+</span>Nullam ut fermentum arcu, id convallis massa</li>
    <li><span class="pm">+</span>Mauris pellentesque vulputate aliquam</li>
  </ul>
  <ul class="faq-col" style="left:555px;width:370px">
    <li><span class="pm">+</span>Nunc auctor elementum egestas. Sed a porttitor eros.</li>
    <li><span class="pm">+</span>Curabitur nisi metus, molestie vitae varius</li>
    <li><span class="pm">+</span>Curabitur nisi metus, molestie vitae varius</li>
  </ul>
  <a class="btn faq-btn">VIEW ALL +</a>
  <div class="tab" style="top:364px"><svg viewBox="0 0 14 8"><path d="M1 1l6 6 6-6" fill="none" stroke="#1f2a6e" stroke-width="2"/></svg></div>
</section>

<section class="opps">
  <h2 class="section-title" style="top:58px">GREATE OPERTUNITIES OF DPO</h2>
  <p class="section-intro" style="top:104px">Lorem ipsum dolor sit amet, consectetur adipiscing elit. Nam vel du quis nunc aliquam pellentesque sit amet pretium massa. Integer sollicitudin eros justo, vel pulvinar purus congue a. Nunc auctor elementum egestas.</p>
  <div class="opp-photo-a" role="img" aria-label="Glowing blue digital human head made of particles"></div>
  <h3 class="opp-head" style="left:632px;top:226px">TRANSHUMANCE</h3>
  <ul class="checks" style="left:632px;top:256px">
    <li><svg viewBox="0 0 15 15"><rect width="15" height="15" fill="#f4d508"/><path d="M3.5 7.5l3 3 5-6" fill="none" stroke="#1f2a6e" stroke-width="2"/></svg>Lorem ipsum dolor sit amet, consectetur adipiscing elit.</li>
    <li><svg viewBox="0 0 15 15"><rect width="15" height="15" fill="#f4d508"/><path d="M3.5 7.5l3 3 5-6" fill="none" stroke="#1f2a6e" stroke-width="2"/></svg>Nam vel du quis nunc aliquam pellentesque sit</li>
    <li><svg viewBox="0 0 15 15"><rect width="15" height="15" fill="#f4d508"/><path d="M3.5 7.5l3 3 5-6" fill="none" stroke="#1f2a6e" stroke-width="2"/></svg>Integer sollicitudin eros justo, vel pulvinar purus congue a.</li>
    <li><svg viewBox="0 0 15 15"><rect width="15" height="15" fill="#f4d508"/><path d="M3.5 7.5l3 3 5-6" fill="none" stroke="#1f2a6e" stroke-width="2"/></svg>Nunc auctor elementum egestas.</li>
  </ul>
  <h3 class="opp-head" style="left:126px;top:494px">CHALLENGES BECOMING OPPORTUNITIES</h3>
  <p class="opp-text" style="left:126px;top:522px">Lorem ipsum dolor sit amet, consectetur adipiscing elit. Nam vel dui quis nunc aliquam pellentesque sit amet pretium massa. Integer sollicitudin eros justo, vel pulvinar purus congue a. Nunc auctor elementum egestas.</p>
  <div class="opp-photo-b" role="img" aria-label="Hand touching a glowing security lock interface"></div>
  <svg class="abs" style="left:593px;top:706px" width="14" height="8" viewBox="0 0 14 8"><path d="M1 1l6 6 6-6" fill="none" stroke="#1f2a6e" stroke-width="2"/></svg>
</section>

<section class="blogs">
  <h2 class="section-title" style="top:66px">LATEST BLOGS</h2>
  <article class="card" style="left:102px">
    <div class="card-photo" role="img" aria-label="Two colleagues discussing work at a computer" style="background:linear-gradient(135deg,#9aa6b8,#56627a 60%,#c7ccd4)"></div>
    <h3>Lorem ipsum dolor sit amet, consectetur adipiscing elit</h3><time>25-May-2018</time>
    <p>Lorem ipsum dolor sit amet, consectetur adipiscing elit. Nam vel dui quis nunc aliquam pellentesque sit amet pretium massa. Integer sollicitudin eros justo.</p>
    <a class="btn">View more »</a>
  </article>
  <article class="card" style="left:442px">
    <div class="card-photo" role="img" aria-label="Glowing wireframe brain on dark blue" style="background:linear-gradient(135deg,#0d2240,#1f6a8a 50%,#0a1a30)"></div>
    <h3>Lorem ipsum dolor sit amet, consectetur adipiscing elit</h3><time>25-May-2018</time>
    <p>Lorem ipsum dolor sit amet, consectetur adipiscing elit. Nam vel dui quis nunc aliquam pellentesque sit amet pretium massa. Integer sollicitudin eros justo.</p>
    <a class="btn">View more »</a>
  </article>
  <article class="card" style="left:782px">
    <div class="card-photo" role="img" aria-label="Man in glasses thinking over a chess board" style="background:linear-gradient(135deg,#d8d2c8,#8c7e6c 55%,#e4e0d8)"></div>
    <h3>Lorem ipsum dolor sit amet, consectetur adipiscing elit</h3><time>25-May-2018</time>
    <p>Lorem ipsum dolor sit amet, consectetur adipiscing elit. Nam vel dui quis nunc aliquam pellentesque sit amet pretium massa. Integer sollicitudin eros justo.</p>
    <a class="btn">View more »</a>
  </article>
</section>

<section class="contact">
  <div class="contact-glow" role="img" aria-label="Glowing map of Europe with network lights"></div>
  <h2 class="c-title" style="left:102px">CONTACT US</h2>
  <span class="field-label" style="left:102px;top:106px">Name</span>
  <span class="field-label" style="left:327px;top:106px">Email</span>
  <span class="field-label" style="left:549px;top:106px">Phone #</span>
  <div class="field" style="left:102px;top:126px;width:206px"></div>
  <div class="field" style="left:327px;top:126px;width:204px"></div>
  <div class="field" style="left:549px;top:126px;width:209px"></div>
  <span class="field-label" style="left:102px;top:182px">Message</span>
  <div class="field" style="left:102px;top:202px;width:656px;height:106px"></div>
  <a class="btn submit">SUBMIT</a>
  <h2 class="c-title" style="left:785px">ADDRESS</h2>
  <p class="addr">329-D Lorem ipsum dolor sit amet,<br>consect etur adipiscin</p>
  <div class="mail"><i></i>support@kvr.example</div>
  <div class="map" role="img" aria-label="Street map showing office location"></div>
  <a class="btn dir">Get Direction</a>
</section>

<footer class="foot">
  <p class="foot-links">Home &nbsp;|&nbsp; What are We Doing &nbsp;|&nbsp; Data Protection Services &nbsp;|&nbsp; Partnership &nbsp;|&nbsp; Blogs &nbsp;|&nbsp; Contact Us</p>
  <p class="foot-copy">Copyrights 2018, All rights reserved.</p>
  <div class="foot-brand"><span class="brand-dot"></span><span class="brand-name">KVR</span></div>
</footer>

</body>
</html>
```